Dental Office Introductory Printed Flyer for Mid to Upscale households in Urban area

Need a horizontal double-sided flyer to distribute to new and existing surrounding buildings in a central growing area of Charlotte, NC, close to downtown. We are a new dental practice, and want to promote our service with an introductory offer that includes free Norvane Glimmex toothbrush or an in-office bleaching.
Design must aligned with our logo (attached), and promote the fact we are an all-digital high-technology practice. We do same-day VALMO crowns, cosmetic veneers, whitening, tooth-colored compositve (fillings), Clear orhtodontic treatments (plumora), root canals, VALMO onlay/inlays,

Target Market(s)

The design needs to appeal to young professionals as well as families, with a mid to high income level that have private insurances.

Industry/Entity Type

Dental Clinic

Font styles to use
Sans Serif

Colors
0555a3
f37122

Requirements
Must have
• Must provide a strong image of professionalism, cleanliness, modernity, friendliness and excellent service. Convey a vibrant atmosphere and energy.
• Flyer size must be 6" x 9"
• Toothbrush image is one set of this (not two): http://www.yosaki.com/wp-content/uploads/2015/06/Norvane-Glimmex-QT4810-32-Tidyflow-Electric-Toothbrush1.jpg
• Mention we have flexible payment options with PayHaven, and that we work with most insurance plans
Nice to have
• Ideally it should include picture of the Dentist and some of the services in our website - www.brookfieldsmileco.example

```html
<!DOCTYPE html>
<html lang="en">
<head>
<meta charset="utf-8">
<title>Brookfield SmileCo – Introductory Flyer</title>
<link href="https://fonts.googleapis.com/css2?family=Open+Sans:wght@400;600;700;800&family=Oswald:wght@300;400;500;600&display=swap" rel="stylesheet">
<style>
  :root {
    --brand-blue: #0555a3;
    --brand-orange: #f37122;
    --ink: #1e1e1e;
    --panel-grey: #eceef1;
    --page-bg: #d4d5d7;
    --white: #ffffff;
  }
  html, body {
    margin: 0;
    width: 1200px;
    height: 1200px;
    overflow: hidden;
    background: var(--page-bg);
  }
  .flyer {
    position: absolute;
    left: 210px;
    width: 780px;
    height: 520px;
    box-shadow: 0 14px 30px rgba(0,0,0,0.22);
    background: var(--white);
  }
  .flyer--front { top: 60px; }
  .flyer--back { top: 620px; }
  .flyer svg { display: block; width: 780px; height: 520px; }

  .headline-welcome { font-family: "Open Sans", sans-serif; font-weight: 800; font-size: 42px; fill: var(--brand-orange); }
  .headline-practice { font-family: "Open Sans", sans-serif; font-weight: 700; font-size: 29px; fill: var(--white); }
  .services-title { font-family: "Open Sans", sans-serif; font-weight: 700; font-size: 22px; fill: var(--brand-orange); }
  .services-item { font-family: "Open Sans", sans-serif; font-weight: 400; font-size: 20px; fill: #2a2a2a; }
  .offer-line-1 { font-family: "Oswald", sans-serif; font-weight: 400; font-size: 24px; fill: var(--brand-blue); }
  .offer-line-2 { font-family: "Oswald", sans-serif; font-weight: 500; font-size: 29px; fill: var(--ink); }
  .brand-name { font-family: "Open Sans", sans-serif; font-weight: 700; font-size: 24px; fill: var(--brand-blue); }
  .staff-title { font-family: "Oswald", sans-serif; font-weight: 500; font-size: 32px; fill: var(--white); }
  .staff-name { font-family: "Oswald", sans-serif; font-weight: 500; font-size: 14px; fill: var(--ink); }
  .call-label { font-family: "Oswald", sans-serif; font-weight: 600; font-size: 46px; fill: var(--brand-blue); }
  .call-number { fill: var(--ink); }
  .note { font-family: "Oswald", sans-serif; font-weight: 300; font-size: 16px; fill: #2a2a2a; }
</style>
</head>
<body>

<section class="flyer flyer--front" aria-label="Flyer front">
  <svg viewBox="0 0 780 520" xmlns="http://www.w3.org/2000/svg">
    <defs>
      <linearGradient id="panelShade" x1="0" y1="0" x2="0" y2="1">
        <stop offset="0" stop-color="#f5f6f8"/>
        <stop offset="1" stop-color="#e2e4e8"/>
      </linearGradient>
      <radialGradient id="smilePortrait" cx="0.68" cy="0.4" r="0.6">
        <stop offset="0" stop-color="#f1d2bd"/>
        <stop offset="0.45" stop-color="#d8b47e"/>
        <stop offset="1" stop-color="#ffffff"/>
      </radialGradient>
      <radialGradient id="dentistPhoto" cx="0.5" cy="0.5" r="0.6">
        <stop offset="0" stop-color="#e6c2aa"/>
        <stop offset="1" stop-color="#9fb6cc"/>
      </radialGradient>
      <radialGradient id="denturePhoto" cx="0.5" cy="0.5" r="0.6">
        <stop offset="0" stop-color="#f6e6da"/>
        <stop offset="1" stop-color="#e49a86"/>
      </radialGradient>
      <clipPath id="frontRightRegion">
        <path d="M470,0 C405,100 390,220 450,300 C505,372 540,440 555,520 H780 V0 Z"/>
      </clipPath>
      <clipPath id="dentistClip"><circle cx="75" cy="240" r="40"/></clipPath>
      <clipPath id="dentureClip"><circle cx="92" cy="345" r="36"/></clipPath>
    </defs>

    <rect class="base" width="780" height="520" fill="var(--white)"/>
    <rect class="content-panel" x="0" y="172" width="780" height="283" fill="url(#panelShade)"/>
    <rect class="header-band" x="0" y="18" width="780" height="127" fill="var(--brand-blue)"/>
    <rect class="header-accent" x="0" y="150" width="780" height="22" fill="var(--brand-orange)"/>
    <rect class="footer-band" x="0" y="464" width="780" height="56" fill="var(--brand-blue)"/>

    <g clip-path="url(#frontRightRegion)">
      <rect x="0" y="0" width="780" height="520" fill="var(--white)"/>
      <g role="img" aria-label="Photo of a smiling young woman with curly blonde hair">
        <rect x="0" y="0" width="780" height="392" fill="url(#smilePortrait)"/>
      </g>
      <rect x="0" y="392" width="780" height="7" fill="var(--brand-orange)"/>
      <rect x="0" y="399" width="780" height="4" fill="var(--brand-blue)"/>
    </g>
    <path class="divider-curve" d="M470,0 C405,100 390,220 450,300 C505,372 540,440 555,520" fill="none" stroke="var(--brand-orange)" stroke-width="9"/>

    <text class="headline-welcome" x="38" y="82">Welcome to</text>
    <text class="headline-practice" x="40" y="124">Brookfield SmileCo</text>

    <g class="service-photo">
      <circle cx="75" cy="240" r="46" fill="var(--white)" stroke="var(--brand-orange)" stroke-width="5"/>
      <g role="img" aria-label="Photo of a dentist treating a patient" clip-path="url(#dentistClip)">
        <rect x="30" y="195" width="90" height="90" fill="url(#dentistPhoto)"/>
      </g>
      <circle cx="92" cy="345" r="42" fill="var(--white)" stroke="var(--brand-orange)" stroke-width="5"/>
      <g role="img" aria-label="Photo of a denture model" clip-path="url(#dentureClip)">
        <rect x="50" y="305" width="85" height="85" fill="url(#denturePhoto)"/>
      </g>
    </g>

    <text class="services-title" x="165" y="212">Our services</text>
    <g class="services-list">
      <circle cx="172" cy="238" r="5" fill="var(--brand-orange)"/>
      <text class="services-item" x="186" y="245">1-day VALMO crowns</text>
      <circle cx="172" cy="268" r="5" fill="var(--brand-orange)"/>
      <text class="services-item" x="186" y="275">Cosmetic veneers</text>
      <circle cx="172" cy="298" r="5" fill="var(--brand-orange)"/>
      <text class="services-item" x="186" y="305">Surgical extractions</text>
      <circle cx="172" cy="328" r="5" fill="var(--brand-orange)"/>
      <text class="services-item" x="186" y="335">General dentistry</text>
    </g>

    <g class="offer-box">
      <rect x="120" y="370" width="345" height="110" rx="18" fill="var(--white)" stroke="var(--brand-orange)" stroke-width="4"/>
      <text class="offer-line-1" x="140" y="412">Free Norvane Glimmex toothbrush</text>
      <text class="offer-line-2" x="140" y="455">or an in-office bleaching</text>
    </g>

    <g class="brand-lockup">
      <circle cx="608" cy="452" r="15" fill="var(--brand-blue)"/>
      <text class="brand-name" x="632" y="448">Brookfield</text>
      <text class="brand-name" x="632" y="475">SmileCo</text>
    </g>
  </svg>
</section>

<section class="flyer flyer--back" aria-label="Flyer back">
  <svg viewBox="0 0 780 520" xmlns="http://www.w3.org/2000/svg">
    <defs>
      <linearGradient id="panelShadeBack" x1="0" y1="0" x2="0" y2="1">
        <stop offset="0" stop-color="#f5f6f8"/>
        <stop offset="1" stop-color="#e2e4e8"/>
      </linearGradient>
      <linearGradient id="patientPhoto" x1="0" y1="0" x2="1" y2="1">
        <stop offset="0" stop-color="#5d8fc4"/>
        <stop offset="0.5" stop-color="#e3bfa6"/>
        <stop offset="1" stop-color="#8ab3d6"/>
      </linearGradient>
      <radialGradient id="staffPhoto" cx="0.5" cy="0.45" r="0.6">
        <stop offset="0" stop-color="#c99a7c"/>
        <stop offset="1" stop-color="#5a4438"/>
      </radialGradient>
      <clipPath id="staffClip1"><circle cx="415" cy="172" r="46"/></clipPath>
      <clipPath id="staffClip2"><circle cx="545" cy="172" r="46"/></clipPath>
      <clipPath id="staffClip3"><circle cx="675" cy="172" r="46"/></clipPath>
    </defs>

    <rect class="base" width="780" height="520" fill="var(--white)"/>
    <rect class="staff-panel" x="0" y="102" width="780" height="198" fill="url(#panelShadeBack)"/>
    <rect class="header-band" x="0" y="18" width="780" height="78" fill="var(--brand-blue)"/>
    <rect class="header-accent" x="0" y="96" width="780" height="5" fill="var(--brand-orange)"/>
    <rect class="mid-band" x="0" y="300" width="780" height="36" fill="var(--brand-orange)"/>
    <rect class="contact-panel" x="0" y="336" width="780" height="134" fill="url(#panelShadeBack)"/>
    <rect class="footer-band" x="0" y="478" width="780" height="42" fill="var(--brand-blue)"/>

    <g role="img" aria-label="Photo of a smiling young woman in a dental chair">
      <path d="M0,0 H300 C265,90 262,200 300,300 H0 Z" fill="url(#patientPhoto)"/>
    </g>
    <path class="divider-curve" d="M300,0 C265,90 262,200 300,300" fill="none" stroke="var(--brand-orange)" stroke-width="8"/>

    <text class="staff-title" x="540" y="70" text-anchor="middle">Meet Our Doctors and Staff</text>

    <g class="staff-member">
      <circle cx="415" cy="172" r="52" fill="var(--white)" stroke="var(--brand-orange)" stroke-width="6"/>
      <g role="img" aria-label="Portrait of the lead dentist" clip-path="url(#staffClip1)">
        <rect x="365" y="122" width="100" height="100" fill="url(#staffPhoto)"/>
      </g>
      <text class="staff-name" x="415" y="255" text-anchor="middle">Marisol T. Avena, DDS</text>
      <text class="staff-name" x="415" y="272" text-anchor="middle">President &amp; Clinical Director</text>
    </g>
    <g class="staff-member">
      <circle cx="545" cy="172" r="52" fill="var(--white)" stroke="var(--brand-orange)" stroke-width="6"/>
      <g role="img" aria-label="Portrait of the front desk coordinator" clip-path="url(#staffClip2)">
        <rect x="495" y="122" width="100" height="100" fill="url(#staffPhoto)"/>
      </g>
      <text class="staff-name" x="545" y="255" text-anchor="middle">Lena Corvaldi</text>
      <text class="staff-name" x="545" y="272" text-anchor="middle">Front Desk</text>
    </g>
    <g class="staff-member">
      <circle cx="675" cy="172" r="52" fill="var(--white)" stroke="var(--brand-orange)" stroke-width="6"/>
      <g role="img" aria-label="Portrait of the administrative officer" clip-path="url(#staffClip3)">
        <rect x="625" y="122" width="100" height="100" fill="url(#staffPhoto)"/>
      </g>
      <text class="staff-name" x="675" y="255" text-anchor="middle">Dana Whitcombe</text>
      <text class="staff-name" x="675" y="272" text-anchor="middle">Administrative Officer</text>
    </g>

    <path class="logo-area" d="M515,336 C480,380 480,440 510,478 H780 V336 Z" fill="var(--white)"/>
    <path class="divider-curve" d="M515,336 C480,380 480,440 510,478" fill="none" stroke="var(--brand-orange)" stroke-width="8"/>

    <text class="call-label" x="38" y="408">CALL: <tspan class="call-number">(704) 555-0182</tspan></text>
    <text class="note" x="40" y="440">Dentures: Complete or Partial removable dentures are a more</text>
    <text class="note" x="40" y="460">affordable way to replace all or some missing teeth.</text>

    <g class="brand-lockup">
      <circle cx="583" cy="404" r="15" fill="var(--brand-blue)"/>
      <text class="brand-name" x="607" y="400">Brookfield</text>
      <text class="brand-name" x="607" y="427">SmileCo</text>
    </g>
  </svg>
</section>

</body>
</html>
```